Letterhead Design Project for online gaming site

We need a letterhead for a new online gaming company. The site is www.lunaroller.co

The logo is a gold colour and the site is similar in nature. Feel free to take a look at the landing page.

However the designer has free reign to do whatever they like with it.

OTHER CONTENT:

Telephone: 1300 746 315
Email: info@lunaroller.co
Web: www.lunaroller.co

Industry/Entity Type

It Company

```html
<!DOCTYPE html>
<html lang="en">
<head>
<meta charset="utf-8">
<title>LunaRoller.co Letterhead</title>
<link href="https://fonts.googleapis.com/css2?family=Inter:wght@300;500&display=swap" rel="stylesheet">
<style>
  :root {
    --backdrop: #bdbdbd;
    --paper: #ffffff;
    --gold: #e2c000;
    --gold-light: #fff05a;
    --gold-deep: #b89600;
    --rule-edge: #3a3420;
    --ink: #222222;
  }
  * { margin: 0; padding: 0; box-sizing: border-box; }
  html, body {
    width: 1200px;
    height: 1000px;
    overflow: hidden;
    background: var(--backdrop);
    font-family: "Inter", Helvetica, Arial, sans-serif;
  }
  .letterhead {
    position: absolute;
    left: 290px;
    top: 62px;
    width: 620px;
    height: 876px;
    background: var(--paper);
  }
  .masthead {
    position: absolute;
    left: 25px;
    right: 25px;
    top: 40px;
    display: flex;
    align-items: flex-end;
    gap: 10px;
  }
  .brand-name {
    font-weight: 500;
    font-size: 33px;
    line-height: 1;
    color: var(--gold-deep);
    letter-spacing: -0.5px;
    white-space: nowrap;
  }
  .gold-rule {
    flex: 1;
    height: 15px;
    margin-bottom: 3px;
    border: 1px solid var(--rule-edge);
    border-radius: 2px;
    background: linear-gradient(to bottom, var(--gold-light) 0%, var(--gold) 45%, var(--gold-deep) 100%);
  }
  .contact-details {
    position: absolute;
    right: 25px;
    top: 95px;
    text-align: right;
    font-weight: 300;
    font-size: 14.5px;
    line-height: 17.5px;
    color: var(--ink);
    list-style: none;
  }
  .footer-rule {
    position: absolute;
    left: 25px;
    right: 25px;
    top: 830px;
    height: 5px;
    border: 1px solid var(--rule-edge);
    border-radius: 2px;
    background: linear-gradient(to bottom, var(--gold-light), var(--gold-deep));
  }
</style>
</head>
<body>
  <main class="letterhead">
    <header class="masthead">
      <span class="brand-name">LunaRoller.co</span>
      <span class="gold-rule"></span>
    </header>
    <ul class="contact-details">
      <li>Telephone: 1300 746 315</li>
      <li>Email: info@lunaroller.co</li>
      <li>Web: www.lunaroller.co</li>
    </ul>
    <div class="footer-rule"></div>
  </main>
</body>
</html>
```